Postcard Design

We are a licensed and insured remodeling contractor in Johnson County, KS. I am looking to get a professional look for our postcard advertising. I would prefer something that appeals to women, but is still masculine enough for a contractor. Here is the verbiage I would like in the postcard.
Ever question the references you get from a contractor? Wouldn't you prefer to get a reference from your neighbor?
We are currently working with one of your neighbors and would love the opportunity to work for you. You can look us up on our website and see some of the wonderful spaces we have helped create. Call us today to schedule an appointment and let us know how we can help you create the new space you have always dreamed of.
Tel: 913-552-0187
Fax:913-530-2814
WWW.BELTRANEHOMEWORKS.EXAMPLE
BELTRANEHOMEWORKS@MAILBOX.EXAMPLE
Here is the verbiage I would like to use.
We are working in your neighborhood.
Tel: 913-552-0187
Fax:913-530-2814
Contractor

```html
<!DOCTYPE html>
<html lang="en">
<head>
<meta charset="utf-8">
<title>Beltrane Homeworks – Neighborhood Postcard</title>
<link rel="stylesheet" href="https://fonts.googleapis.com/css2?family=Mulish:wght@300;400;800&display=swap">
<style>
  :root {
    --navy: #1b2b3b;
    --navy-deep: #132130;
    --orange: #f7941d;
    --orange-line: #c98a3c;
    --white: #ffffff;
    --mist: #d6d9dc;
    --slate: #7b93a6;
    --ink: #2a2f36;
    --ground: #1e1e1e;
  }
  * { box-sizing: border-box; margin: 0; padding: 0; }
  html, body { width: 1200px; height: 1200px; overflow: hidden; background: var(--ground); }
  body { font-family: "Mulish", sans-serif; }

  .stage { position: absolute; left: 0; top: 0; width: 1000px; height: 1000px; transform: scale(1.2); transform-origin: 0 0; }

  .card { position: absolute; overflow: hidden; }

  /* ---------- reverse side ---------- */
  .card-back { left: 349px; top: 22px; width: 606px; height: 465px; background: var(--white); }
  .back-panel { position: absolute; left: 0; top: 0; width: 293px; height: 388px; }
  .back-panel-dark { position: absolute; left: 0; top: 0; width: 293px; height: 238px; background: var(--navy); }
  .tile { position: absolute; width: 64px; height: 64px; background: var(--orange); }
  .tile.photo { border: 2px solid var(--orange-line); padding: 3px; background: var(--navy); }
  .tile.photo .fill { width: 100%; height: 100%; }
  .intro { position: absolute; left: 9px; top: 152px; width: 278px; color: var(--white); font-size: 13px; line-height: 15.2px; font-weight: 400; }
  .back-panel-light { position: absolute; left: 0; top: 238px; width: 293px; height: 145px; background: linear-gradient(180deg, #ffffff 0%, #eceeef 55%, #c9ccd0 100%); }
  .call { position: absolute; left: 9px; top: 6px; width: 278px; color: var(--ink); font-size: 13px; line-height: 15.2px; }
  .call strong { color: var(--slate); font-weight: 800; font-size: 16px; letter-spacing: 0.2px; }
  .back-contacts { position: absolute; left: 9px; top: 82px; color: var(--ink); font-size: 13.5px; line-height: 17.5px; }
  .back-panel-bar { position: absolute; left: 0; top: 383px; width: 293px; height: 5px; background: var(--orange); }

  .contact-row { display: flex; align-items: center; gap: 5px; white-space: nowrap; }
  .contact-row svg { flex: none; }
  .contact-row .gap { display: inline-block; width: 14px; }

  .brand { display: flex; align-items: center; gap: 6px; color: var(--navy); font-weight: 800; white-space: nowrap; }
  .brand-mark { display: block; background: var(--navy); }
  .back-brand { position: absolute; left: 302px; top: 58px; font-size: 12.5px; }
  .back-brand .brand-mark { width: 11px; height: 11px; }
  .stamp-box { position: absolute; left: 459px; top: 8px; width: 139px; height: 139px; border: 1px solid #b9bcbf; }

  /* ---------- front side ---------- */
  .card-front { left: 53px; top: 512px; width: 609px; height: 468px; background: linear-gradient(135deg, var(--navy) 0%, var(--navy-deep) 100%); }
  .frame { position: absolute; border: 1.5px solid var(--orange-line); padding: 3px; }
  .frame .fill { width: 100%; height: 100%; }
  .headline-box { position: absolute; left: 309px; top: 21px; width: 279px; height: 134px; background: var(--orange); color: var(--white); text-align: center; font-weight: 300; }
  .headline-small { margin-top: 32px; font-size: 19.5px; }
  .headline-big { font-size: 39px; line-height: 42px; }
  .question-box { position: absolute; left: 309px; top: 168px; width: 279px; height: 133px; border: 1px solid var(--orange-line); padding: 18px 10px 0 8px; color: var(--white); font-size: 16.6px; line-height: 22px; font-weight: 300; }
  .question { display: flex; gap: 7px; margin-bottom: 9px; }
  .question svg { flex: none; margin-top: 5px; }
  .contact-band { position: absolute; left: 0; top: 316px; width: 609px; height: 137px; background: linear-gradient(180deg, #ffffff 0%, #f1f2f3 50%, var(--mist) 100%); }
  .band-edge { position: absolute; top: 0; width: 22px; height: 137px; background: var(--orange); }
  .band-edge.left { left: 0; }
  .band-edge.right { right: 0; }
  .front-brand { position: absolute; left: 40px; top: 55px; font-size: 20px; }
  .front-brand .brand-mark { width: 18px; height: 18px; }
  .front-contacts { position: absolute; left: 306px; top: 29px; color: var(--ink); font-size: 14.5px; line-height: 22.5px; }
</style>
</head>
<body>
<div class="stage">

  <section class="card card-back" aria-label="Postcard reverse side">
    <div class="back-panel">
      <div class="back-panel-dark">
        <div class="tile" style="left:9px;top:8px"></div>
        <div class="tile photo" style="left:79px;top:8px"><div class="fill" role="img" aria-label="Photo of a remodeled laundry room with washer and dryer" style="background:linear-gradient(160deg,#b7b2a6,#77736c)"></div></div>
        <div class="tile" style="left:149px;top:8px"></div>
        <div class="tile photo" style="left:219px;top:8px"><div class="fill" role="img" aria-label="Photo of a dining room with table and chairs" style="background:linear-gradient(160deg,#a89478,#4a3a2c)"></div></div>
        <div class="tile photo" style="left:9px;top:79px"><div class="fill" role="img" aria-label="Photo of a finished hallway with wood floor" style="background:linear-gradient(160deg,#d9c9b0,#7a5a3e)"></div></div>
        <div class="tile" style="left:79px;top:79px"></div>
        <div class="tile photo" style="left:149px;top:79px"><div class="fill" role="img" aria-label="Photo of a remodeled bathroom" style="background:linear-gradient(160deg,#d8cbb6,#9a8466)"></div></div>
        <div class="tile" style="left:219px;top:79px"></div>
        <p class="intro">We are currently working with one of your neighbors and would love the opportunity to work for you. You can look us up on our website and see some of the wonderful spaces we have helped create.</p>
      </div>
      <div class="back-panel-light">
        <p class="call"><strong>CALL US TODAY</strong> to schedule an appointment and let us know how we can help you create the new space you have always dreamed of.</p>
        <div class="back-contacts">
          <div class="contact-row">
            <svg width="9" height="13" viewBox="0 0 9 13"><path d="M6 0.5 L8.5 1.5 L7.5 4 L5.5 4 Q4.5 6.5 5.5 9 L7.5 9 L8.5 11.5 L6 12.5 Q1 10 1 6.5 Q1 3 6 0.5Z" fill="var(--orange)"/></svg>
            <span>913-552-0187</span><span class="gap"></span>
            <svg width="11" height="13" viewBox="0 0 11 13"><path d="M5 0.5 L7.5 1.5 L6.5 4 L4.5 4 Q3.5 6.5 4.5 9 L6.5 9 L7.5 11.5 L5 12.5 Q0 10 0 6.5 Q0 3 5 0.5Z" fill="var(--orange)"/><rect x="7" y="3" width="4" height="5" fill="none" stroke="var(--orange)" stroke-width="1"/></svg>
            <span>913-530-2814</span>
          </div>
          <div class="contact-row">
            <svg width="10" height="10" viewBox="0 0 10 10"><circle cx="5" cy="5" r="4.3" fill="none" stroke="var(--orange)" stroke-width="1.2"/><path d="M0.7 5 H9.3 M5 0.7 Q2.5 5 5 9.3 M5 0.7 Q7.5 5 5 9.3" fill="none" stroke="var(--orange)" stroke-width="0.9"/></svg>
            <span>www.beltranehomeworks.example</span>
          </div>
          <div class="contact-row">
            <svg width="10" height="8" viewBox="0 0 10 8"><rect x="0.5" y="0.5" width="9" height="7" rx="1" fill="var(--orange)"/><path d="M0.8 1 L5 4.5 L9.2 1" fill="none" stroke="#fff" stroke-width="0.8"/></svg>
            <span>beltranehomeworks@mailbox.example</span>
          </div>
        </div>
      </div>
      <div class="back-panel-bar"></div>
    </div>
    <div class="brand back-brand"><span class="brand-mark"></span><span>Beltrane Homeworks</span></div>
    <div class="stamp-box"></div>
  </section>

  <section class="card card-front" aria-label="Postcard front side">
    <div class="frame" style="left:22px;top:21px;width:274px;height:134px"><div class="fill" role="img" aria-label="Photo of a two-storey house exterior with garage under blue sky" style="background:linear-gradient(180deg,#3f74b8 0%,#8fb0d6 35%,#a39a7c 55%,#7d7560 100%)"></div></div>
    <div class="headline-box">
      <p class="headline-small">We are working in your</p>
      <p class="headline-big">neighborhood</p>
    </div>
    <div class="frame" style="left:22px;top:168px;width:133px;height:132px"><div class="fill" role="img" aria-label="Photo of a remodeled kitchen with wood cabinets and window" style="background:linear-gradient(160deg,#a56b34 0%,#e8e4da 45%,#6b4a2e 100%)"></div></div>
    <div class="frame" style="left:163px;top:168px;width:133px;height:132px"><div class="fill" role="img" aria-label="Photo of a bathroom with tub and tiled floor" style="background:linear-gradient(160deg,#c9a574 0%,#dfe3e8 50%,#9aa6b6 100%)"></div></div>
    <div class="question-box">
      <div class="question">
        <svg width="12" height="12" viewBox="0 0 12 12"><rect x="0" y="0" width="5.3" height="5.3" fill="var(--orange)"/><rect x="6.7" y="0" width="5.3" height="5.3" fill="var(--orange)"/><rect x="0" y="6.7" width="5.3" height="5.3" fill="var(--orange)"/><rect x="6.7" y="6.7" width="5.3" height="5.3" fill="var(--orange)"/></svg>
        <p>Ever question the references you get from a contractor?</p>
      </div>
      <div class="question">
        <svg width="12" height="12" viewBox="0 0 12 12"><rect x="0" y="0" width="5.3" height="5.3" fill="var(--orange)"/><rect x="6.7" y="0" width="5.3" height="5.3" fill="var(--orange)"/><rect x="0" y="6.7" width="5.3" height="5.3" fill="var(--orange)"/><rect x="6.7" y="6.7" width="5.3" height="5.3" fill="var(--orange)"/></svg>
        <p>Wouldn't you prefer to get a reference from your neighbor?</p>
      </div>
    </div>
    <div class="contact-band">
      <div class="band-edge left"></div>
      <div class="band-edge right"></div>
      <div class="brand front-brand"><span class="brand-mark"></span><span>Beltrane Homeworks</span></div>
      <div class="front-contacts">
        <div class="contact-row">
          <svg width="9" height="13" viewBox="0 0 9 13"><path d="M6 0.5 L8.5 1.5 L7.5 4 L5.5 4 Q4.5 6.5 5.5 9 L7.5 9 L8.5 11.5 L6 12.5 Q1 10 1 6.5 Q1 3 6 0.5Z" fill="var(--orange)"/></svg>
          <span>913-552-0187</span>
        </div>
        <div class="contact-row">
          <svg width="11" height="13" viewBox="0 0 11 13"><path d="M5 0.5 L7.5 1.5 L6.5 4 L4.5 4 Q3.5 6.5 4.5 9 L6.5 9 L7.5 11.5 L5 12.5 Q0 10 0 6.5 Q0 3 5 0.5Z" fill="var(--orange)"/><rect x="7" y="3" width="4" height="5" fill="none" stroke="var(--orange)" stroke-width="1"/></svg>
          <span>913-530-2814</span>
        </div>
        <div class="contact-row">
          <svg width="11" height="11" viewBox="0 0 10 10"><circle cx="5" cy="5" r="4.3" fill="none" stroke="var(--orange)" stroke-width="1.2"/><path d="M0.7 5 H9.3 M5 0.7 Q2.5 5 5 9.3 M5 0.7 Q7.5 5 5 9.3" fill="none" stroke="var(--orange)" stroke-width="0.9"/></svg>
          <span>www.beltranehomeworks.example</span>
        </div>
        <div class="contact-row">
          <svg width="11" height="9" viewBox="0 0 10 8"><rect x="0.5" y="0.5" width="9" height="7" rx="1" fill="var(--orange)"/><path d="M0.8 1 L5 4.5 L9.2 1" fill="none" stroke="#fff" stroke-width="0.8"/></svg>
          <span>beltranehomeworks@mailbox.example</span>
        </div>
      </div>
    </div>
  </section>

</div>
</body>
</html>
```